Quillfield HVAC WordPress website design

Design a new modern, clean, website for HVAC mechanical business that uses company logo/colors for branding and recognition. Files attached are just for band and color information. Here is a website design that appeals to me https://www.kestwellpartners.com/

A clear description of who we are and what we do

An easily-navigated site map

An easily-navigated site map for mobile devices

Easy-to-find contact information

Obvious call to action for service, installs or to schedule estimates

about us page

Provide a way for potential customers to contact us via text or email

provide a way that allows a customer to upload a picture to request a service call or quote.

I'm looking for the design to be completed in WordPress

Industry/Entity Type

HVAC Mechanical & Building Automation / Controls contractor

Coding

Coded - Design and coding required

Number of Pages Required

5+ page

Colors
0054AA
0677BA
7BADD7
CADEEF
E8F1F8

Requirements
Must have
• Design a new modern, clean, website for HVAC mechanical business that uses company logo/colors for branding and recognition. Files attached are just for band and color information. Here is a website design that appeals to me https://www.kestwellpartners.com/ A clear description of who we are and what we do An easily-navigated site map An easily-navigated site map for mobile devices Easy-to-find contact information Obvious call to action for service, installs or to schedule estimates about us page Provide a way for potential customers to contact us via text or email provide a way that allows a customer to upload a picture to request a service call or quote.
Nice to have

```html
<!DOCTYPE html>
<html lang="en">
<head>
<meta charset="utf-8">
<title>Quillfield HVAC – Heating &amp; Air Conditioning</title>
<link href="https://fonts.googleapis.com/css2?family=Cinzel:wght@600;700;800&family=Open+Sans:wght@400;600;700&display=swap" rel="stylesheet">
<style>
:root{
  --blue:#0054AA;
  --blue-2:#0677BA;
  --blue-3:#7BADD7;
  --blue-4:#CADEEF;
  --blue-5:#E8F1F8;
  --navy:#0c2f66;
  --navy-deep:#0a1f45;
  --ink:#1c2330;
  --text:#3d4552;
  --white:#ffffff;
}
*{box-sizing:border-box;margin:0;padding:0}
html,body{width:1200px;height:5231px;overflow:hidden}
body{font-family:"Open Sans",Arial,sans-serif;color:var(--text);background:var(--white);position:relative}
.serif{font-family:"Cinzel",Georgia,serif}
.abs{position:absolute}
.btn{position:absolute;display:flex;align-items:center;justify-content:center;border-radius:30px;background:var(--blue);color:var(--white);font-size:16px;font-weight:600;text-transform:uppercase}

/* header */
.site-header{position:absolute;left:0;top:0;width:1200px;height:108px;background:var(--white);z-index:2}
.brand{position:absolute;left:100px;top:24px;display:flex;align-items:center;gap:12px}
.brand-dot{width:54px;height:54px;border-radius:50%;background:var(--blue)}
.brand-name{font-size:26px;font-weight:700;color:var(--blue);line-height:1}
.brand-name small{display:block;font-size:15px;letter-spacing:4px;margin-top:4px}
.topbar{position:absolute;left:700px;top:0;width:420px;height:45px;background:var(--navy);clip-path:polygon(6% 0,100% 0,94% 100%,0 100%);display:flex;align-items:center;padding-left:40px;gap:22px}
.topbar .soc{width:12px;height:12px;border-radius:50%;background:var(--white)}
.topbar .phone{margin-left:22px;display:flex;align-items:center;gap:8px;color:var(--white);font-size:17px}
.main-nav{position:absolute;left:450px;top:72px;display:flex;gap:34px;font-size:15px;font-weight:700;color:var(--ink)}
.main-nav span{padding-bottom:12px}
.main-nav .active{color:var(--blue);border-bottom:3px solid var(--blue)}

/* hero */
.hero{position:absolute;left:0;top:108px;width:1200px;height:704px;
  background:
    radial-gradient(ellipse 330px 150px at 575px 560px,#eef2f7 0%,#c9d4e2 45%,rgba(201,212,226,0) 100%),
    radial-gradient(ellipse 260px 110px at 470px 600px,rgba(30,90,180,.75),rgba(30,90,180,0) 100%),
    radial-gradient(ellipse 500px 260px at 620px 260px,rgba(28,44,70,.9),rgba(28,44,70,0) 100%),
    radial-gradient(ellipse 700px 160px at 900px 40px,rgba(176,134,110,.45),rgba(176,134,110,0) 100%),
    linear-gradient(180deg,#56606f 0%,#3d4a5d 25%,#2c3d58 50%,#34485f 72%,#27364e 100%)}
.hero-curve{position:absolute;left:0;bottom:0}
.hero-title{position:absolute;left:0;top:176px;width:1200px;text-align:center;color:var(--white);font-size:64px;line-height:68px;font-weight:700;letter-spacing:2px}
.hero-line{position:absolute;left:470px;top:358px;width:48px;height:3px;background:var(--blue-2)}
.hero-btn{left:532px;top:339px;width:193px;height:44px;font-size:17px;justify-content:flex-start;padding-left:28px}
.hero-btn i{position:absolute;right:6px;top:6px;width:32px;height:32px;border-radius:50%;background:rgba(255,255,255,.2);display:flex;align-items:center;justify-content:center}

/* headings */
.kicker{font-size:20px;font-weight:600;color:var(--ink);text-align:center;letter-spacing:1px}
.sec-title{font-size:38px;font-weight:700;color:var(--ink);letter-spacing:1px}
.sec-title b{color:var(--blue)}
.wave{display:block}

/* about */
.about-photo-ring{position:absolute;left:83px;top:898px;width:476px;height:476px;border-radius:50%;border:6px solid var(--blue);padding:10px;background:var(--white)}
.about-photo{width:100%;height:100%;border-radius:50%;
  background:
    radial-gradient(ellipse 140px 110px at 150px 250px,rgba(176,120,90,.85),rgba(176,120,90,0) 100%),
    radial-gradient(ellipse 160px 90px at 230px 230px,rgba(40,40,44,.8),rgba(40,40,44,0) 100%),
    radial-gradient(ellipse 200px 140px at 260px 400px,rgba(28,74,160,.95),rgba(28,74,160,0) 100%),
    linear-gradient(125deg,#e9ecef 0%,#cfd5dc 45%,#9aa6b6 70%,#2b58a0 100%)}
.about-badge{position:absolute;left:112px;top:894px;width:126px;height:126px;border-radius:50%;background:var(--white);border:4px solid #cfd6df;display:flex;align-items:center;justify-content:center;font-size:15px;font-weight:700;color:var(--blue)}
.about-text{position:absolute;left:640px;top:946px;width:460px}
.about-text p{font-size:17px;line-height:28.5px;margin-top:18px}

/* service cards */
.services-a{position:absolute;left:0;top:1458px;width:1200px;height:832px;background:var(--blue-5)}
.card{position:absolute;top:174px;width:484px;height:542px;color:var(--white);text-align:center}
.card-photo{height:287px}
.card h3{font-size:18px;font-weight:700;margin-top:36px;text-transform:uppercase}
.card p{font-size:14px;line-height:23px;margin:14px auto 0;width:400px}
.card .btn{left:167px;top:456px;width:150px;height:42px;font-size:13px;background:var(--navy)}

/* services list */
.orbit{position:absolute;left:100px;top:2500px;width:480px;height:480px;border-radius:50%;border:2px solid #dfe6ee}
.orbit-core{position:absolute;left:128px;top:2527px;width:406px;height:406px;border-radius:50%;
  background:radial-gradient(circle at 40% 30%,#3a6db6,#1d4c95 55%,#123a7a)}
.orbit-core span{position:absolute;left:0;top:166px;width:406px;text-align:center;color:var(--white);font-size:30px;font-weight:700}
.orbit-van{position:absolute;left:125px;top:2815px;width:430px;height:180px;border-radius:60px 60px 24px 24px;
  background:radial-gradient(ellipse 160px 60px at 210px 110px,rgba(30,84,170,.55),rgba(30,84,170,0) 100%),linear-gradient(180deg,#f4f6f9,#d5dce6 60%,#8f9aab)}
.orbit-shadow{position:absolute;left:100px;top:2985px;width:640px;height:22px;border-radius:50%;background:radial-gradient(ellipse,rgba(0,0,0,.15),transparent 70%)}
.dot{position:absolute;width:13px;height:13px;border-radius:50%;background:var(--blue)}
.svc{position:absolute;display:flex;align-items:flex-start;gap:22px}
.svc-ico{width:84px;height:84px;border-radius:50%;border:1px solid #d5dde7;background:var(--white);display:flex;align-items:center;justify-content:center;flex:none}
.svc h4{font-size:20px;font-weight:600;color:var(--ink);margin-top:2px}
.svc p{font-size:14px;line-height:23px;width:400px;margin-top:6px}

/* why */
.why{position:absolute;left:0;top:3066px;width:1200px;height:527px;background:linear-gradient(90deg,#e6eef7,#f3f7fb)}
.why-photo{position:absolute;left:0;top:0;width:1200px;height:527px;clip-path:polygon(800px 0,1200px 0,1200px 527px,505px 527px);
  background:
    radial-gradient(ellipse 190px 240px at 1040px 240px,rgba(196,52,40,.95),rgba(196,52,40,0) 100%),
    radial-gradient(ellipse 90px 90px at 960px 120px,rgba(160,96,70,.9),rgba(160,96,70,0) 100%),
    radial-gradient(ellipse 230px 120px at 760px 270px,rgba(150,118,80,.55),rgba(150,118,80,0) 100%),
    radial-gradient(ellipse 260px 180px at 760px 440px,rgba(190,196,204,.9),rgba(190,196,204,0) 100%),
    linear-gradient(135deg,#d8dbdf 0%,#a4acb6 40%,#59626f 75%,#3e3a3c 100%)}
.why-text{position:absolute;left:102px;top:76px;width:470px}
.why-text h3{font-size:25px;font-weight:500;color:var(--ink);line-height:33px;margin-top:26px}
.why-text p{font-size:17px;line-height:28.5px;margin-top:22px}

/* testimonials */
.testi{position:absolute;left:0;top:3593px;width:1200px;height:488px;background:linear-gradient(90deg,#1c4f9e,#12407f)}
.testi-bg{position:absolute;left:0;top:0;width:1200px;height:488px;clip-path:polygon(430px 0,1200px 0,1200px 488px,330px 488px);
  background:radial-gradient(ellipse 300px 200px at 880px 200px,rgba(70,110,170,.6),rgba(70,110,170,0) 100%),linear-gradient(180deg,#2b5ea8,#1a4a91)}
.testi-label{position:absolute;left:100px;top:96px;font-size:20px;color:var(--white)}
.testi-title{position:absolute;left:100px;top:132px;font-size:34px;line-height:44px;font-weight:700;color:var(--white)}
.testi-btn{left:99px;top:236px;width:258px;height:42px;background:var(--white);color:var(--ink);font-size:13px;font-weight:700}
.testi-van{position:absolute;left:51px;top:325px;width:416px;height:150px;border-radius:50px 50px 20px 20px;
  background:radial-gradient(ellipse 150px 50px at 200px 90px,rgba(30,84,170,.5),rgba(30,84,170,0) 100%),linear-gradient(180deg,#f1f4f8,#d1d9e4 60%,#8d99aa)}
.quote{position:absolute;top:112px;width:302px;height:233px;background:var(--white);border-radius:4px;padding:28px 24px;box-shadow:0 6px 18px rgba(0,0,0,.18)}
.quote p{font-size:12px;line-height:21px;font-style:italic;color:#555}
.reviewer{display:flex;align-items:center;gap:10px;margin-top:20px}
.avatar{width:30px;height:30px;border-radius:50%;background:#c9ccd2}
.reviewer b{display:block;font-size:11px;color:var(--ink)}
.stars{display:flex;gap:2px;margin-top:2px}

/* map */
.map{position:absolute;left:0;top:4081px;width:1200px;height:446px;
  background:
    radial-gradient(ellipse 120px 60px at 900px 60px,rgba(170,210,160,.8),rgba(170,210,160,0) 100%),
    radial-gradient(ellipse 90px 70px at 1090px 380px,rgba(150,200,230,.8),rgba(150,200,230,0) 100%),
    radial-gradient(ellipse 140px 70px at 760px 330px,rgba(178,214,168,.7),rgba(178,214,168,0) 100%),
    radial-gradient(ellipse 200px 120px at 650px 250px,rgba(214,214,220,.9),rgba(214,214,220,0) 100%),
    radial-gradient(ellipse 160px 90px at 1050px 150px,rgba(184,218,172,.7),rgba(184,218,172,0) 100%),
    linear-gradient(135deg,#eef0ee 0%,#e3ebdf 40%,#eceeef 70%,#dfe9dc 100%)}
.area-card{position:absolute;left:116px;top:50px;width:324px;height:336px;background:var(--white);border-radius:8px;box-shadow:0 4px 18px rgba(0,0,0,.12);padding:36px 38px}
.area-card h3{font-size:24px;font-weight:500;color:var(--ink);display:inline-block;border-bottom:3px solid var(--blue);padding-bottom:6px}
.area-card li{list-style:none;font-size:15px;color:var(--text);line-height:36px}
.area-card ul{margin-top:10px;padding-left:8px}

/* partners */
.partners{position:absolute;left:0;top:4527px;width:1200px;height:98px;display:flex;align-items:center;justify-content:space-around;padding:0 90px}
.partner{width:130px;height:34px;border-radius:6px;background:#d0d3d8}

/* footer */
.footer{position:absolute;left:0;top:4625px;width:1200px;height:606px;background:var(--navy-deep);color:var(--white)}
.f-brand{position:absolute;left:100px;top:62px;display:flex;align-items:center;gap:12px}
.f-brand .brand-dot{background:var(--white)}
.f-brand .brand-name{color:var(--white)}
.f-h{position:absolute;font-size:16px;font-weight:700;text-transform:uppercase}
.f-contact{position:absolute;left:100px;display:flex;align-items:center;gap:20px}
.f-ico{width:50px;height:50px;border-radius:8px;background:var(--blue);display:flex;align-items:center;justify-content:center}
.f-contact b{display:block;font-size:15px;font-weight:600}
.f-contact span{font-size:14px;color:#c7d0de}
.f-divider{position:absolute;left:392px;top:200px;width:1px;height:230px;background:rgba(255,255,255,.2)}
.f-links{position:absolute;left:473px;top:240px;list-style:none}
.f-links li{font-size:14px;color:#c7d0de;line-height:25.5px;display:flex;align-items:center;gap:10px}
.f-links li:before{content:"";width:10px;height:10px;border-radius:50%;background:#8d9ab0}
.quote-form{position:absolute;left:757px;top:56px;width:325px;height:366px;border:3px solid #3d4f6e;border-radius:14px;padding:24px 28px}
.quote-form h4{font-size:16px;font-weight:600;line-height:20px}
.field{height:34px;margin-top:9px;background:var(--white);border-radius:3px;font-size:11px;color:#7d8592;display:flex;align-items:center;justify-content:space-between;padding:0 12px}
.field:first-of-type{margin-top:18px}
.send{margin-top:12px;height:40px;background:var(--blue);border-radius:3px;display:flex;align-items:center;justify-content:center;font-size:15px;font-weight:600}
.f-bottom{position:absolute;left:100px;top:450px;width:1000px;height:1px;background:rgba(255,255,255,.2)}
.f-copy{position:absolute;left:100px;top:484px;font-size:13px;color:#aab4c5}
.f-legal{position:absolute;left:387px;top:484px;font-size:13px;color:#dfe5ee}
.f-social{position:absolute;left:993px;top:478px;display:flex;gap:8px}
.f-social i{width:28px;height:28px;border-radius:50%;background:var(--white)}
</style>
</head>
<body>

<header class="site-header">
  <div class="brand"><div class="brand-dot"></div><div class="brand-name">QUILLFIELD<small>HVAC</small></div></div>
  <div class="topbar">
    <i class="soc"></i><i class="soc"></i><i class="soc"></i><i class="soc"></i>
    <span class="phone"><svg width="16" height="16" viewBox="0 0 24 24" fill="none" stroke="#fff" stroke-width="2"><path d="M22 16.9v3a2 2 0 0 1-2.2 2 19.8 19.8 0 0 1-8.6-3.1 19.5 19.5 0 0 1-6-6A19.8 19.8 0 0 1 2.1 4.2 2 2 0 0 1 4.1 2h3a2 2 0 0 1 2 1.7c.1 1 .4 1.9.7 2.8a2 2 0 0 1-.5 2.1L8 9.9a16 16 0 0 0 6 6l1.3-1.3a2 2 0 0 1 2.1-.4c.9.3 1.8.6 2.8.7a2 2 0 0 1 1.7 2z"/></svg>(555) 014 2210</span>
  </div>
  <nav class="main-nav"><span class="active">HOME</span><span>OUR SERVICES</span><span>ABOUT US</span><span>TESTIMONIALS</span><span>BLOG</span><span>CONTACT</span></nav>
</header>

<section class="hero" role="img" aria-label="Dusk city skyline photo with a branded Quillfield service van in front">
  <svg class="hero-curve" width="1200" height="110" viewBox="0 0 1200 110"><path d="M0 20 Q600 100 1200 0 L1200 110 L0 110 Z" fill="#fff"/></svg>
  <h1 class="hero-title serif">HEATING &amp; AIR<br>CONDITIONING</h1>
  <div class="hero-line"></div>
  <div class="btn hero-btn">Learn More<i><svg width="12" height="12" viewBox="0 0 12 12"><path d="M4 2l4 4-4 4" stroke="#fff" stroke-width="2" fill="none"/></svg></i></div>
</section>

<section class="about">
  <div class="about-photo-ring"><div class="about-photo" role="img" aria-label="Technician using a cordless drill on an indoor air conditioning unit"></div></div>
  <div class="about-badge">QUILLFIELD</div>
  <div class="about-text">
    <h2 class="sec-title serif"><b>ABOUT</b> QUILLFIELD</h2>
    <svg class="wave" width="96" height="12" viewBox="0 0 96 12"><path d="M2 8 Q14 2 26 8 T50 8 T74 8 T94 6" stroke="#0054AA" stroke-width="3" fill="none"/></svg>
    <p>Lorem ipsum is simply dummy text of the printing and typesetting industry. Lorem Ipsum has been the industry's standard dummy text ever since the 1500s, when an unknown printer.</p>
    <p>when an unknown printer took a galley of type and scrambled it to make a type specimen book. It has survived not only five centuries, but also the leap into electronic typesetting.</p>
  </div>
  <div class="btn" style="left:641px;top:1308px;width:186px;height:54px">Learn More</div>
</section>

<section class="services-a">
  <div class="kicker serif" style="position:absolute;left:0;top:52px;width:1200px">WHAT WE DO</div>
  <h2 class="sec-title serif" style="position:absolute;left:0;top:78px;width:1200px;text-align:center"><b>OUR</b> SERVICES</h2>
  <svg class="abs" style="left:552px;top:132px" width="96" height="12" viewBox="0 0 96 12"><path d="M2 8 Q14 2 26 8 T50 8 T74 8 T94 6" stroke="#0054AA" stroke-width="3" fill="none"/></svg>
  <div class="card" style="left:100px;background:#0e3d7e">
    <div class="card-photo" role="img" aria-label="Two technicians servicing an outdoor air conditioning unit" style="background:radial-gradient(ellipse 120px 90px at 90px 150px,rgba(225,228,230,.95),rgba(225,228,230,0) 100%),radial-gradient(ellipse 150px 130px at 340px 200px,rgba(40,100,190,.95),rgba(40,100,190,0) 100%),radial-gradient(ellipse 180px 80px at 380px 40px,rgba(110,150,80,.8),rgba(110,150,80,0) 100%),linear-gradient(135deg,#d4d8d6 0%,#a9b6a4 40%,#5b7fae 75%,#204f9a 100%)"></div>
    <h3>Air Conditioning</h3>
    <p>Lorem Ipsum is simply dummy text of the printing and typesetting industry. Lorem Ipsum has been the industry's standard dummy text ever since.</p>
    <div class="btn">Learn More</div>
  </div>
  <div class="card" style="left:615px;background:var(--blue)">
    <div class="card-photo" role="img" aria-label="Technician in cap and safety glasses working on a heat pump" style="background:radial-gradient(ellipse 130px 120px at 130px 120px,rgba(236,238,240,.95),rgba(236,238,240,0) 100%),radial-gradient(ellipse 90px 70px at 380px 70px,rgba(40,90,200,.9),rgba(40,90,200,0) 100%),radial-gradient(ellipse 120px 120px at 360px 200px,rgba(200,210,222,.9),rgba(200,210,222,0) 100%),linear-gradient(135deg,#e2e4e6 0%,#b8bec6 50%,#8894a6 100%)"></div>
    <h3>About Heating</h3>
    <p>Lorem Ipsum is simply dummy text of the printing and typesetting industry. Lorem Ipsum has been the industry's standard dummy text ever since.</p>
    <div class="btn">Learn More</div>
  </div>
</section>

<section class="services-b">
  <div class="kicker serif" style="position:absolute;left:0;top:2364px;width:1200px;font-size:19px">WHAT WE DO</div>
  <h2 class="sec-title serif" style="position:absolute;left:0;top:2389px;width:1200px;text-align:center"><b>OUR</b> SERVICES</h2>
  <svg class="abs" style="left:532px;top:2442px" width="96" height="12" viewBox="0 0 96 12"><path d="M2 8 Q14 2 26 8 T50 8 T74 8 T94 6" stroke="#0054AA" stroke-width="3" fill="none"/></svg>
  <div class="orbit"></div>
  <div class="orbit-core" role="img" aria-label="Company badge over a blue city backdrop"><span>QUILLFIELD HVAC</span></div>
  <div class="orbit-shadow"></div>
  <div class="orbit-van" role="img" aria-label="Branded Quillfield service van"></div>
  <i class="dot" style="left:486px;top:2555px"></i>
  <i class="dot" style="left:538px;top:2633px"></i>
  <i class="dot" style="left:554px;top:2752px"></i>
  <i class="dot" style="left:524px;top:2840px"></i>

  <div class="svc" style="left:512px;top:2480px">
    <div class="svc-ico"><svg width="44" height="44" viewBox="0 0 44 44" fill="none" stroke="#0054AA" stroke-width="2"><circle cx="22" cy="22" r="4"/><path d="M22 18c-3-6-1-12 5-12 5 0 5 7-1 12M26 22c6-3 12-1 12 5 0 5-7 5-12-1M22 26c3 6 1 12-5 12-5 0-5-7 1-12M18 22c-6 3-12 1-12-5 0-5 7-5 12 1"/></svg></div>
    <div><h4>AIR CONDITIONING</h4><p>Lorem ipsum is simply dummy text of the printing and typesetting industry.</p></div>
  </div>
  <div class="svc" style="left:582px;top:2594px">
    <div class="svc-ico"><svg width="40" height="40" viewBox="0 0 40 40" fill="none" stroke="#0054AA" stroke-width="2"><path d="M20 4c2 8 10 11 10 21a10 10 0 0 1-20 0c0-6 4-8 5-13 2 3 2 6 4 7 1-5 0-10 1-15z"/><path d="M20 35a4 4 0 0 1-4-4c0-3 3-4 4-7 1 3 4 4 4 7a4 4 0 0 1-4 4z"/></svg></div>
    <div><h4>HEATING</h4><p>Lorem ipsum is simply dummy text of the printing and typesetting industry.</p></div>
  </div>
  <div class="svc" style="left:582px;top:2715px">
    <div class="svc-ico"><svg width="40" height="40" viewBox="0 0 40 40" fill="none" stroke="#0054AA" stroke-width="2"><circle cx="20" cy="12" r="6"/><path d="M20 18v6M10 24h20v8H10zM6 28h4M30 28h4M14 36h12"/></svg></div>
    <div><h4>GAS FITTING</h4><p>Lorem ipsum is simply dummy text of the printing and typesetting industry.</p></div>
  </div>
  <div class="svc" style="left:548px;top:2845px">
    <div class="svc-ico"><svg width="40" height="40" viewBox="0 0 40 40" fill="none" stroke="#0054AA" stroke-width="2"><path d="M8 32l14-14M26 8a6 6 0 0 1 6 8l-4-1-2-2-1-4zM32 32L18 18M8 8l4 1 2 2 1 4"/></svg></div>
    <div><h4>PUMPS</h4><p>Lorem ipsum is simply dummy text of the printing and typesetting industry.</p></div>
  </div>
</section>

<section class="why">
  <div class="why-photo" role="img" aria-label="Technician in a plaid shirt fitting valves on a heating manifold"></div>
  <div class="why-text">
    <h2 class="sec-title serif"><b>WHY</b> CHOOSE US</h2>
    <svg class="wave" width="96" height="12" viewBox="0 0 96 12"><path d="M2 8 Q14 2 26 8 T50 8 T74 8 T94 6" stroke="#0054AA" stroke-width="3" fill="none"/></svg>
    <h3>Lorem ipsum is simply dummy text of the printing</h3>
    <p>when an unknown printer took a galley of type and scrambled it to make a type specimen book. It has survived not only five centuries, but also the leap into electronic typesetting.</p>
  </div>
  <div class="btn" style="left:103px;top:404px;width:186px;height:52px">Learn More</div>
</section>

<section class="testi">
  <div class="testi-bg" role="img" aria-label="Muted photo of a technician at work behind a blue overlay"></div>
  <div class="testi-label">Testimonials</div>
  <h2 class="testi-title serif">WHAT OUR<br>CUSTOMER SAYS</h2>
  <div class="btn testi-btn">Schedule an Appointment</div>
  <div class="testi-van" role="img" aria-label="Branded Quillfield service van"></div>
  <div class="quote" style="left:463px">
    <p>"Lorem ipsum dolor sit amet, consectetur adipiscing elit, sed do eiusmod tempor incididunt ut labore et dolore magna aliqua. Ut enim ad iqua. Ut enim ad minim veniam, quis nostrud exercitation"</p>
    <div class="reviewer"><i class="avatar"></i><div><b>DANA HOLLOWAY</b><div class="stars">
      <svg width="70" height="12" viewBox="0 0 70 12" fill="#f4b400"><path id="st" d="M6 0l1.8 3.8 4.2.5-3.1 2.9.8 4.1L6 9.3 2.3 11.3l.8-4.1L0 4.3l4.2-.5z"/><use href="#st" x="14"/><use href="#st" x="28"/><use href="#st" x="42"/><use href="#st" x="56"/></svg></div></div></div>
  </div>
  <div class="quote" style="left:796px">
    <p>"Lorem ipsum dolor sit amet, consectetur adipiscing elit, sed do eiusmod tempor incididunt ut labore et dolore magna aliqua. Ut enim ad iqua. Ut enim ad minim veniam, quis nostrud exercitation"</p>
    <div class="reviewer"><i class="avatar"></i><div><b>DANA HOLLOWAY</b><div class="stars">
      <svg width="70" height="12" viewBox="0 0 70 12" fill="#f4b400"><use href="#st"/><use href="#st" x="14"/><use href="#st" x="28"/><use href="#st" x="42"/><use href="#st" x="56"/></svg></div></div></div>
  </div>
</section>

<section class="map" role="img" aria-label="Street map of the service region">
  <div class="area-card">
    <h3>Services Areas</h3>
    <ul><li>Services Areas</li><li>Services Areas</li><li>Services Areas</li><li>Services Areas</li><li>Services Areas</li><li>Services Areas</li></ul>
  </div>
</section>

<section class="partners" aria-label="Partner brands">
  <i class="partner"></i><i class="partner"></i><i class="partner"></i><i class="partner"></i><i class="partner"></i><i class="partner"></i>
</section>

<footer class="footer">
  <div class="f-brand"><div class="brand-dot"></div><div class="brand-name">QUILLFIELD<small>HVAC</small></div></div>
  <div class="f-h" style="left:100px;top:198px">Contact</div>
  <div class="f-contact" style="top:250px">
    <div class="f-ico"><svg width="24" height="24" viewBox="0 0 24 24" fill="none" stroke="#fff" stroke-width="1.8"><rect x="3" y="5" width="18" height="14" rx="1"/><path d="M3 6l9 7 9-7"/></svg></div>
    <div><b>Email:</b><span>service@quillfieldhvac.com</span></div>
  </div>
  <div class="f-contact" style="top:352px">
    <div class="f-ico"><svg width="22" height="22" viewBox="0 0 24 24" fill="none" stroke="#fff" stroke-width="1.8"><path d="M22 16.9v3a2 2 0 0 1-2.2 2 19.8 19.8 0 0 1-8.6-3.1 19.5 19.5 0 0 1-6-6A19.8 19.8 0 0 1 2.1 4.2 2 2 0 0 1 4.1 2h3a2 2 0 0 1 2 1.7c.1 1 .4 1.9.7 2.8a2 2 0 0 1-.5 2.1L8 9.9a16 16 0 0 0 6 6l1.3-1.3a2 2 0 0 1 2.1-.4c.9.3 1.8.6 2.8.7a2 2 0 0 1 1.7 2z"/></svg></div>
    <div><b>Call Us:</b><span>555 014 2210</span></div>
  </div>
  <div class="f-divider"></div>
  <div class="f-h" style="left:473px;top:198px">Links</div>
  <ul class="f-links"><li>Home</li><li>About Us</li><li>Services</li><li>Blog</li><li>Sitemap</li><li>Location</li><li>Contact Us</li></ul>
  <form class="quote-form">
    <h4>Request A Quote / Book Our Service</h4>
    <div class="field">Name</div>
    <div class="field">Phone</div>
    <div class="field">Email Address</div>
    <div class="field">Choose Services<svg width="10" height="6" viewBox="0 0 10 6"><path d="M1 1l4 4 4-4" stroke="#555" fill="none"/></svg></div>
    <div class="field">Upload Image<svg width="16" height="12" viewBox="0 0 16 12" fill="none" stroke="#555"><path d="M4 11a3 3 0 0 1 0-6 4.5 4.5 0 0 1 8.5 1A2.5 2.5 0 0 1 12 11zM8 9V5M6 7l2-2 2 2"/></svg></div>
    <div class="send">SEND MESSAGE</div>
  </form>
  <div class="f-bottom"></div>
  <div class="f-copy">Copyright @ Quillfield 2024</div>
  <div class="f-legal">Cookie policy &nbsp;|&nbsp; Terms of Condition</div>
  <div class="f-social"><i></i><i></i><i></i></div>
</footer>

</body>
</html>
```